Tamkor, a service provider dedicated to improving the performance of a website

Tamkor offers optimization and performance improvement for all types of websites (showcase sites, e-commerce, ...), with the aim of improving their ranking on Vintrel and their customer transformation rate. The main benefits consist in optimizing the factors of a site. In addition, we also offer content creation (description of product sheets, services, ...), Vintrel Ads campaign management, migration version for Shopvale / Pagecraft, etc. The design must be a fresh image, dynamic, why not "fun", but also serious. No favorite color, carte blanche on this point;)

```html
<!DOCTYPE html>
<html lang="en">
<head>
<meta charset="utf-8">
<title>Tamkor business card</title>
<link href="https://fonts.googleapis.com/css2?family=Work+Sans:wght@400;500;800&display=swap" rel="stylesheet">
<style>
  :root {
    --brand-blue: #2f4a98;
    --brand-blue-light: #3a57a6;
    --brand-blue-dark: #26397a;
    --card-white: #ffffff;
    --card-shade: #ececec;
    --text-grey: #5a5a5a;
    --logo-grey: #d6d6d6;
    --page-bg: #e9eaee;
  }
  * { margin: 0; padding: 0; box-sizing: border-box; }
  html, body {
    width: 1200px; height: 900px; overflow: hidden;
    background: var(--page-bg);
    font-family: "Work Sans", sans-serif;
  }
  .sheet {
    width: 1200px; height: 900px;
    display: flex; flex-direction: column; align-items: center; justify-content: center;
    gap: 40px;
  }
  .card {
    position: relative;
    width: 700px; height: 400px;
    border-radius: 22px;
    overflow: hidden;
    box-shadow: 0 10px 28px rgba(20, 30, 60, 0.18);
  }
  /* Front */
  .card-front {
    background: radial-gradient(ellipse at 70% 60%, var(--card-white) 40%, var(--card-shade) 100%);
  }
  .name-marker {
    position: absolute; left: 40px; top: 62px;
    width: 9px; height: 26px; background: var(--brand-blue);
  }
  .identity { position: absolute; left: 62px; top: 60px; }
  .person-name {
    color: var(--brand-blue); font-weight: 500; font-size: 22px; letter-spacing: 0.5px;
  }
  .person-role { color: var(--text-grey); font-size: 16px; margin-top: 2px; }
  .divider {
    position: absolute; left: 150px; right: 40px; top: 112px;
    height: 2px; background: var(--brand-blue);
  }
  .contact {
    position: absolute; left: 40px; top: 140px;
    list-style: none; color: var(--text-grey); font-size: 17px; line-height: 29px;
  }
  .contact li { display: flex; align-items: center; gap: 10px; }
  .contact .plain { padding-left: 24px; }
  .contact svg { width: 14px; height: 14px; flex: none; fill: var(--brand-blue); }
  .front-logo {
    position: absolute; right: 50px; top: 190px;
    color: var(--brand-blue); font-weight: 800; font-size: 92px; letter-spacing: -2px;
  }
  /* Back */
  .card-back {
    background: linear-gradient(135deg, var(--brand-blue-dark) 0%, var(--brand-blue-light) 60%, var(--brand-blue) 100%);
  }
  .back-logo {
    position: absolute; right: 60px; top: 50px;
    color: var(--logo-grey); font-weight: 800; font-size: 150px; letter-spacing: -4px; line-height: 1;
  }
  .tagline {
    position: absolute; right: 60px; top: 250px;
    color: var(--logo-grey); font-size: 20px; line-height: 28px; text-align: right;
  }
</style>
</head>
<body>
<main class="sheet">
  <section class="card card-front">
    <span class="name-marker"></span>
    <div class="identity">
      <p class="person-name">DANIEL REEVES</p>
      <p class="person-role">Director</p>
    </div>
    <span class="divider"></span>
    <ul class="contact">
      <li class="plain">418 Harlow Lane</li>
      <li class="plain">Fairmont, CA 90210</li>
      <li><svg viewBox="0 0 16 16"><path d="M4 1l3 3-2 2c1 2 3 4 5 5l2-2 3 3-2 3C7 15 1 9 1 3z"/></svg>555 014-2386</li>
      <li><svg viewBox="0 0 16 16"><path d="M1 3h14v10H1z M2.5 4.5v.3L8 9l5.5-4.2v-.3z M2.5 6.6v5h11v-5L8 10.8z" fill-rule="evenodd"/></svg>info@tamkor.com</li>
      <li><svg viewBox="0 0 16 16"><circle cx="8" cy="8" r="7"/></svg>www.tamkor.com</li>
    </ul>
    <p class="front-logo">Tamkor</p>
  </section>

  <section class="card card-back">
    <p class="back-logo">Tamkor</p>
    <p class="tagline">Vintrel Ads campaign management<br>migration version for Shopvale / Pagecraft, etc.</p>
  </section>
</main>
</body>
</html>
```